Building quality affordable homes in Brisbane, Australia for investors and families

We design, build and market our own homes from small single story to large 3 story luxury homes. Our main focus is "duel key" - that is two houses on one lot - a "zooky" (as in where The Zook lived) or attached granny flat.
We have a logo design and need a business card to suit. Something simple but eye catching. We want to communicate: "you are making a smart financial choice buying or building with us".
Unfortunately a lot of information has to be on the card including - Name, position, phone, mobile, fax, email, web address and of course the logo.
Logo in multiple formats and high res now available.

Target Market(s)

Families, contractors, real estate agents, other builders, developers, banks and home buyers.

Industry/Entity Type

Financial

Contact Information for Business Card

Name, position, phone, mobile, fax, email, web address

Font styles to use
Serif

Requirements
Must have
• The logo, and the details.
Nice to have
• Show or explain what we do - design, build and market affordable homes.
Should not have
• Nothing too fancy, outrageous - building companies are normally very straight.

```html
<!DOCTYPE html>
<html lang="en">
<head>
<meta charset="utf-8">
<title>Brightwell Homes – Business Card</title>
<link rel="stylesheet" href="https://fonts.googleapis.com/css2?family=Open+Sans:wght@400;600;700&display=swap">
<style>
  :root {
    --backdrop: #e9e6e2;
    --card-white: #ffffff;
    --sky: #8fb3e0;
    --sky-deep: #7aa6dc;
    --band-grey: #c9c9c9;
    --band-dark: #505254;
    --slate: #55595c;
    --brand-blue: #1a86c8;
    --ink-grey: #5a5a5a;
  }
  * { box-sizing: border-box; margin: 0; padding: 0; }
  html, body { width: 1200px; height: 914px; overflow: hidden; }
  body {
    background: var(--backdrop);
    font-family: "Open Sans", Arial, sans-serif;
    display: flex;
    align-items: center;
    justify-content: center;
    gap: 40px;
  }
  .card {
    position: relative;
    width: 540px;
    height: 310px;
    overflow: hidden;
    box-shadow: 0 6px 18px rgba(0,0,0,0.18);
  }

  /* Front */
  .card-front { background: var(--card-white); }
  .front-blue {
    position: absolute; left: 0; right: 0; bottom: 0; top: 140px;
    background: linear-gradient(120deg, var(--sky) 0%, #9bbce4 45%, var(--sky-deep) 100%);
  }
  .front-white-step {
    position: absolute; left: 270px; right: 0; top: 140px; height: 30px;
    background: var(--card-white);
  }
  .band-light {
    position: absolute; left: 0; width: 270px; top: 120px; height: 20px;
    background: var(--band-grey);
    display: flex; align-items: center; gap: 12px; padding-left: 54px;
    color: var(--ink-grey); font-size: 11px;
  }
  .band-dark {
    position: absolute; left: 270px; right: 0; top: 170px; height: 20px;
    background: var(--band-dark);
    display: flex; align-items: center; gap: 12px; padding-left: 60px;
    color: #ffffff; font-size: 11px;
  }
  .brand {
    position: absolute; display: flex; align-items: center; gap: 12px;
  }
  .brand-mark { width: 56px; height: 56px; flex: none; }
  .brand-name { font-weight: 700; font-size: 26px; white-space: nowrap; }
  .card-front .brand { left: 92px; top: 30px; }
  .card-front .brand-mark { background: var(--sky); }
  .card-front .brand-name { color: var(--brand-blue); }

  .person {
    position: absolute; left: 54px; top: 150px; color: #ffffff;
  }
  .person-name { font-size: 17px; font-weight: 600; letter-spacing: 0.5px; text-transform: uppercase; }
  .person-role { font-size: 10px; margin-top: -2px; }
  .contact-list {
    position: absolute; left: 40px; top: 200px; list-style: none; color: #ffffff; font-size: 12px;
  }
  .contact-list li { display: flex; align-items: center; gap: 12px; height: 20px; }
  .icon { width: 12px; height: 12px; flex: none; }

  /* Back */
  .card-back { background: var(--slate); }
  .card-back .brand { left: 60px; top: 118px; }
  .card-back .brand-mark { background: #ffffff; width: 70px; height: 70px; }
  .card-back .brand-name { color: #ffffff; font-size: 32px; }
</style>
</head>
<body>

<section class="card card-front" aria-label="Business card, front">
  <div class="front-blue"></div>
  <div class="front-white-step"></div>

  <div class="brand">
    <span class="brand-mark"></span>
    <span class="brand-name">Brightwell Homes Pty Ltd</span>
  </div>

  <div class="band-light">
    <svg class="icon" viewBox="0 0 12 12" fill="#1a86c8" aria-hidden="true"><circle cx="6" cy="3.5" r="2.8"/><path d="M0.5 12 C0.5 7.5 11.5 7.5 11.5 12 Z"/></svg>
    <span>013 246 5780</span>
  </div>

  <div class="band-dark">
    <svg class="icon" viewBox="0 0 12 12" fill="#ffffff" aria-hidden="true"><path d="M2.4 0.5 L4.4 3 L3.2 4.3 C3.9 5.9 5.6 7.8 7.7 8.8 L8.9 7.6 L11.5 9.6 L10.2 11.5 C5.2 11 1 6.8 0.5 1.8 Z"/></svg>
    <span>986 543 2107</span>
  </div>

  <div class="person">
    <p class="person-name">Martin Hale</p>
    <p class="person-role">Managing Director</p>
  </div>

  <ul class="contact-list">
    <li>
      <svg class="icon" viewBox="0 0 12 12" fill="#ffffff" aria-hidden="true"><rect x="3" y="0.5" width="6" height="3"/><rect x="0.5" y="4" width="11" height="5" rx="1"/><rect x="3" y="8" width="6" height="3.5"/></svg>
      <span>0000 222 000</span>
    </li>
    <li>
      <svg class="icon" viewBox="0 0 12 12" fill="none" stroke="#ffffff" stroke-width="1.3" aria-hidden="true"><rect x="0.7" y="2" width="10.6" height="8"/><path d="M0.7 2 L6 6.5 L11.3 2"/></svg>
      <span>info@brightwellhomes.com</span>
    </li>
    <li>
      <svg class="icon" viewBox="0 0 12 12" fill="none" stroke="#ffffff" stroke-width="1.1" aria-hidden="true"><circle cx="6" cy="6" r="5.3"/><ellipse cx="6" cy="6" rx="2.3" ry="5.3"/><path d="M0.7 6 H11.3"/></svg>
      <span>www.brightwellhomes.com</span>
    </li>
  </ul>
</section>

<section class="card card-back" aria-label="Business card, back">
  <div class="brand">
    <span class="brand-mark"></span>
    <span class="brand-name">Brightwell Homes</span>
  </div>
</section>

</body>
</html>
```